Website Design for a High School

School Name: Bayt Nakhla Private Schools
sub-schools:
1-Bayt Nakhla Primary School
2-Bayt Nakhla High School for Girls
3-Bayt Nakhla High School for Boys
The design should be professional and serious and below is the details of the website.
Pages: (Home, About Us, Schools, Events, Students, Gallery, Lectures, Contact Us).
A-) Home Page:
1-Animated photos banner as main
2-Marquee for the last news.
3-Welcoming block of text
4-latest news at the body of the page.
5-Calender "on the side"
6-Number of visitors "on the side"
7-Search bar
8-options to choose a school
B-) School Page:
three schools listed as drop down menu when highlighted over the Schools button in the menu
*Each school page should contain:
1-Student login area
2-Animation photos header
3-Specific news and projects
C-) Student Login page:
have a Report Card
D-) Gallery Page
have a collection of photos.
E-)Contact Page
phone numbers
emails
feedback form
F-)Other mentioned pages
with normal text and photos page look as similar to the Home page.
Required color: Purple as main and include the logo colors
Logo: is attached.
Button link to change language to Arabic.
School
5+ page

```html
<!DOCTYPE html>
<html lang="en">
<head>
<meta charset="utf-8">
<title>Bayt Nakhla Private Schools</title>
<link href="https://fonts.googleapis.com/css2?family=Lato:wght@400;700;900&family=Walter+Turncoat&display=swap" rel="stylesheet">
<style>
:root{
  --yellow:#fcc856;
  --yellow-dark:#f2b638;
  --nav-active:#9e7c3d;
  --purple:#4c4679;
  --beige:#efeee1;
  --panel:#eeede0;
  --ink:#3a3a3a;
  --grey:#8d8d8d;
  --light:#f5f5f5;
  --band:#454545;
  --field:#5b5b5b;
}
*{margin:0;padding:0;box-sizing:border-box}
html,body{width:689px;height:1200px;overflow:hidden;background:#fff}
body{position:relative;font-family:'Lato',sans-serif;color:var(--ink)}
.abs{position:absolute}
.display{font-family:'Walter Turncoat',cursive}

.topbar{left:0;top:0;width:689px;height:20px;background:var(--light);border-bottom:1px solid #e6e6e6;font-size:6px;color:var(--grey)}
.topbar .item{top:6px;display:flex;align-items:center;gap:5px}
.topbar .social{top:0;width:22px;height:20px;border-left:1px solid #e4e4e4}

.logo{left:100px;top:30px;width:72px;height:72px;border-radius:50%;border:3px solid var(--purple);display:flex;align-items:center;justify-content:center;text-align:center;font-weight:900;font-size:10px;line-height:1.15;color:var(--purple)}
.tagline{font-family:'Walter Turncoat',cursive;font-size:8.5px;color:var(--yellow-dark);letter-spacing:.3px}
.search{left:193px;top:66px;width:161px;height:22px;border:1px solid #e2e2e2;border-radius:11px;background:#fafafa;font-size:6px;color:#999;padding:7px 0 0 14px}
.search .btn{position:absolute;right:5px;top:4px;width:29px;height:13px;border-radius:7px;background:var(--yellow)}
.info-small{font-size:7.5px;color:#777}
.info-big{font-size:9.5px;font-weight:700;color:#444}

.nav{left:0;top:113px;width:689px;height:27px;background:var(--yellow)}
.nav .active{left:99px;top:0;width:46px;height:27px;background:var(--nav-active)}
.nav a{position:absolute;top:9px;font-family:'Walter Turncoat',cursive;font-size:7px;color:#fff;text-decoration:none;letter-spacing:.3px}
.nav .dot{position:absolute;top:13px;width:2px;height:2px;background:#fff;border-radius:50%}

.hero{left:0;top:140px;width:689px;height:245px;background:linear-gradient(90deg,#7a3f26 0%,#9a5536 30%,#8b4a2e 60%,#7b3f25 100%)}
.board{left:278px;top:155px;width:320px;height:214px;border:8px solid #a56a36;background:linear-gradient(135deg,#3a3a3a,#262626);box-shadow:0 2px 6px rgba(0,0,0,.4)}
.board .b1{left:20px;top:36px;font-size:10px;color:var(--yellow);letter-spacing:.5px}
.board .rule{left:20px;top:54px;width:170px;border-top:1px dashed #888}
.board .b2{left:20px;top:74px;font-size:14px;color:#fff;letter-spacing:1px}
.board .b3{left:20px;top:107px;font-size:8.5px;color:#ddd;letter-spacing:1px}
.board .b4{left:20px;top:124px;font-size:14px;color:#eee;letter-spacing:2.5px}
.board .join{left:19px;top:154px;width:114px;height:28px;background:var(--yellow);color:#fff;font-size:9px;text-align:center;line-height:28px;letter-spacing:1px}
.arrow-btn{width:30px;height:30px;border-radius:50%;background:rgba(255,255,255,.85);display:flex;align-items:center;justify-content:center}

.marquee{left:0;top:385px;width:689px;height:25px;background:var(--yellow);font-size:5.5px;color:#fff;white-space:nowrap;padding:9px 0 0 99px;overflow:hidden}
.marquee span{margin-right:14px}

.welcome{left:0;top:438px;width:689px;text-align:center;font-size:13.5px;letter-spacing:1px;color:#444}
.welcome em{font-style:normal;color:var(--yellow)}

.panel{top:490px;width:163px;height:213px;background:var(--panel)}
.panel h2{height:26px;background:var(--purple);color:#fff;font-family:'Walter Turncoat',cursive;font-weight:400;font-size:10.5px;text-align:center;line-height:27px;letter-spacing:.8px}
.more-circle{top:689px;width:29px;height:29px;border-radius:50%;background:var(--panel);border:2px solid #ddd9c5;display:flex;align-items:center;justify-content:center}

.news{left:11px;width:145px;height:42px}
.news .thumb{left:0;top:0;width:40px;height:40px;border:2px solid #fff}
.news .title{left:46px;top:0;font-size:7px;font-weight:700;color:#444}
.news .date{left:46px;top:13px;font-size:5.5px;color:#999}
.news .pill{left:65px;top:12px;width:55px;height:9px;background:#cfcdbd;font-size:5.5px;color:#555;padding:1.5px 0 0 6px}
.news .text{left:46px;top:24px;width:100px;font-size:5px;line-height:7px;color:#888}
.news .text b{color:#555}

.visitors .total{left:0;top:38px;width:163px;text-align:center;font-size:12px;color:#666}
.counter{left:15px;top:62px;display:flex;gap:1px}
.counter span{width:16px;height:22px;background:#fff;border:1px solid #ddd;font-size:8px;color:#666;text-align:center;line-height:21px}
.visitors .join{left:0;top:97px;width:163px;text-align:center;font-size:11.5px;letter-spacing:.8px;color:#555}
.vrow{left:12px;width:140px;height:22px;border-bottom:1px solid #dcdaca;font-size:8px;color:#555}
.vrow .lab{left:4px;top:6px}
.vrow .cell{top:0;width:16px;height:21px;background:#d1cfbf;font-size:7px;color:#fff;text-align:center;line-height:21px}

.promo{left:0;top:745px;width:689px;height:200px;background:linear-gradient(90deg,#eef3f6 0%,#dfe8ef 45%,#c9d9e6 70%,#b8cde0 100%)}
.promo .t1{left:99px;top:28px;font-size:27px;color:#333;letter-spacing:1px}
.promo .t2{left:180px;top:57px;font-size:6.5px;color:#444;font-style:italic}
.promo .t3{left:145px;top:70px;font-size:24px;color:#333;letter-spacing:1px}
.promo .t4{left:148px;top:102px;font-size:10px;color:#333;letter-spacing:1px}
.promo .t4 small{font-size:5px}
.promo .more{left:147px;top:126px;width:59px;height:20px;border-radius:10px;background:var(--yellow);color:#fff;font-size:7px;text-align:center;line-height:20px}
.tab{top:925px;height:20px;font-family:'Walter Turncoat',cursive;font-size:6px;text-align:center;line-height:21px}
.tab.on{background:var(--band);color:var(--yellow)}
.tab.off{background:#f0f0f0;color:#555}

.finder{left:0;top:945px;width:689px;height:55px;background:var(--band)}
.field{top:18px;height:19px;background:var(--field);font-size:6px;color:#ccc;padding:6px 0 0 8px}
.send{top:18px;left:513px;width:77px;height:19px;background:var(--yellow);color:#fff;font-family:'Walter Turncoat',cursive;font-size:7px;text-align:center;line-height:20px}

.footer{left:0;top:1000px;width:689px;height:175px;background:var(--beige)}
.footer h3{position:absolute;top:32px;font-family:'Walter Turncoat',cursive;font-weight:400;font-size:9.5px;color:#333;letter-spacing:.8px}
.footer .line{top:50px;height:1px;background:var(--yellow)}
.input{left:99px;width:131px;background:#d6d4c3;font-size:5px;color:#fff;padding:5px 0 0 8px}
.fsend{left:185px;top:121px;width:46px;height:19px;border-radius:10px;background:var(--yellow);border:1px solid #e0aa3a;color:#fff;font-size:6px;text-align:center;line-height:17px}
.gallery{left:275px;top:64px;display:grid;grid-template-columns:repeat(3,35px);gap:2px}
.gallery span{height:23px;border:1px solid #fff}
.detail{left:428px;width:100px;height:28px;border-bottom:1px solid #e0decd;font-size:6px;color:#666}
.detail svg{position:absolute;left:1px;top:9px}
.detail .v{position:absolute;right:0;top:10px}
.social-sq{left:571px;width:19px;height:19px}

.copyright{left:0;top:1175px;width:689px;height:25px;background:var(--purple);color:#fff;font-size:6.5px;text-align:center;line-height:25px;letter-spacing:.3px}
</style>
</head>
<body>

<header>
  <div class="abs topbar">
    <div class="abs item" style="left:107px">
      <svg width="9" height="7" viewBox="0 0 9 7"><rect x=".5" y=".5" width="8" height="6" fill="none" stroke="#999"/><path d="M.5 .5 4.5 4 8.5 .5" fill="none" stroke="#999"/></svg>
      <span>info@baytnakhla.edu</span>
    </div>
    <div class="abs item" style="left:202px">
      <svg width="6" height="8" viewBox="0 0 6 8"><path d="M3 8C1 5 0 4 0 3a3 3 0 0 1 6 0c0 1-1 2-3 5z" fill="#999"/></svg>
      <span>14-B, Nakhla District</span>
    </div>
    <div class="abs social" style="left:501px"></div>
    <div class="abs social" style="left:523px"></div>
    <div class="abs social" style="left:545px"></div>
    <div class="abs social" style="left:567px;border-right:1px solid #e4e4e4"></div>
  </div>

  <div class="abs logo">Bayt<br>Nakhla</div>

  <div class="abs tagline" style="left:193px;top:44px">BEST SERVICES FOR YOUR KIDS</div>
  <div class="abs search">Search
    <div class="btn"><svg width="29" height="13" viewBox="0 0 29 13"><circle cx="13.5" cy="6" r="2.5" fill="none" stroke="#fff"/><path d="M15.3 7.8 17 9.5" stroke="#fff"/></svg></div>
  </div>

  <div class="abs tagline" style="left:375px;top:44px">SCHOOL HOURS !</div>
  <svg class="abs" style="left:373px;top:65px" width="22" height="22" viewBox="0 0 22 22"><circle cx="11" cy="11" r="9.5" fill="none" stroke="var(--yellow)" stroke-width="1.5"/><path d="M11 5v6h4" fill="none" stroke="var(--yellow)" stroke-width="1.5"/></svg>
  <div class="abs info-small" style="left:400px;top:65px">5 Days Weekly</div>
  <div class="abs info-big" style="left:400px;top:76px">8:30 am - 6:00 pm</div>
  <svg class="abs" style="left:490px;top:66px" width="22" height="22" viewBox="0 0 22 22"><path d="M5 3c2 0 3 4 2 5l-1 1c1 3 4 6 7 7l1-1c1-1 5 0 5 2l-1 2c-6 1-16-9-15-15z" fill="none" stroke="var(--yellow)" stroke-width="1.4"/><path d="M13 4a6 6 0 0 1 5 5M13 7a3 3 0 0 1 2 2" fill="none" stroke="var(--yellow)" stroke-width="1.2"/></svg>
  <div class="abs info-small" style="left:517px;top:66px">Contact Phone</div>
  <div class="abs info-big" style="left:517px;top:77px">+9124-5678-901</div>

  <nav class="abs nav">
    <div class="abs active"></div>
    <a style="left:110px">HOME</a>
    <span class="dot" style="left:155px"></span>
    <a style="left:167px">ABOUT US</a>
    <span class="dot" style="left:216px"></span>
    <a style="left:227px">STUDENTS</a>
    <span class="dot" style="left:280px"></span>
    <a style="left:292px">LECTURES</a>
    <span class="dot" style="left:346px"></span>
    <a style="left:357px">SCHOOLS</a>
    <span class="dot" style="left:407px"></span>
    <a style="left:418px">GALLERY</a>
    <span class="dot" style="left:467px"></span>
    <a style="left:479px">EVENTS</a>
    <span class="dot" style="left:523px"></span>
    <a style="left:536px">CONTACT US</a>
  </nav>
</header>

<section class="abs hero" role="img" aria-label="Photo of a young boy in glasses and suspenders in front of a brick wall">
  <div class="abs arrow-btn" style="left:33px;top:108px"><svg width="10" height="10" viewBox="0 0 10 10"><path d="M6 1 2 5l4 4V6h3V4H6z" fill="#555"/></svg></div>
  <div class="abs arrow-btn" style="left:627px;top:108px"><svg width="10" height="10" viewBox="0 0 10 10"><path d="M4 1l4 4-4 4V6H1V4h3z" fill="#555"/></svg></div>
</section>
<div class="abs board">
  <div class="abs display b1">BAYT NAKHLA SCHOOLS ✓</div>
  <div class="abs rule"></div>
  <div class="abs display b2">WELCOME &amp; HELLO !</div>
  <div class="abs display b3">PERFECT EDUCATION FOR</div>
  <div class="abs display b4">YOUR CHILD.</div>
  <div class="abs display join">JOIN US</div>
</div>

<div class="abs marquee">
  <span>Lorem ipsum dolor sit amet, consectetuer ...</span>•&nbsp;&nbsp;
  <span>Sed diam nonummy nibh euismod tincidu...</span>•&nbsp;&nbsp;
  <span>Laoreet dolore magna aliquam erat volut...</span>•&nbsp;&nbsp;
  <span>Enim ad minim veniam, quis</span>
</div>

<h1 class="abs display welcome" style="font-weight:400">WELCOME TO THE <em>BAYT NAKHLA SCHOOLS !</em></h1>
<div class="abs" style="left:258px;top:466px;width:172px;height:1px;background:#e4e4e4"></div>
<div class="abs" style="left:330px;top:465px;width:28px;height:2px;background:var(--yellow)"></div>

<section class="abs panel" style="left:99px">
  <h2>LATEST NEWS</h2>
  <div class="abs news" style="top:40px">
    <div class="abs thumb" role="img" aria-label="Children in a classroom" style="background:linear-gradient(135deg,#e7b37a,#c9775a)"></div>
    <div class="abs title">Bayt Nakhla Schools ...</div>
    <div class="abs date">Date :</div><div class="abs pill">28 May 2015</div>
    <div class="abs text">Lorem ipsum dolor sit amet, consectetr adipiscing elit, sed diam ...<b>Read More</b></div>
  </div>
  <div class="abs news" style="top:94px">
    <div class="abs thumb" role="img" aria-label="Children drawing together" style="background:linear-gradient(135deg,#9cc6e0,#e9c48e)"></div>
    <div class="abs title">Classes with happy childs...</div>
    <div class="abs date">Date :</div><div class="abs pill">28 May 2015</div>
    <div class="abs text">Lorem ipsum dolor sit amet, consectetr adipiscing elit, sed diam ...<b>Read More</b></div>
  </div>
  <div class="abs news" style="top:148px">
    <div class="abs thumb" role="img" aria-label="Pupils at their desks" style="background:linear-gradient(135deg,#d8e6f0,#8cb0d0)"></div>
    <div class="abs title">Bayt Nakhla Schools ...</div>
    <div class="abs date">Date :</div><div class="abs pill">28 May 2015</div>
    <div class="abs text">Lorem ipsum dolor sit amet, consectetr adipiscing elit, sed diam ...<b>Read More</b></div>
  </div>
</section>

<section class="abs panel" style="left:263px">
  <h2>CALENDER</h2>
  <svg class="abs" style="left:0;top:26px" width="163" height="187" viewBox="0 0 163 187" font-family="Lato, sans-serif" font-size="5.5" text-anchor="middle">
    <g fill="#666">
      <text x="16" y="22">Mon</text><text x="37" y="22">Tue</text><text x="61" y="22">Wes</text><text x="83" y="22">Thu</text><text x="105" y="22">Fri</text><text x="127" y="22">Sat</text><text x="148" y="22">Sun</text>
    </g>
    <rect x="10" y="117" width="145" height="12" rx="6" fill="var(--yellow)" transform="translate(45 -28) scale(.75 1) translate(-2 0)"/>
    <rect x="53" y="81" width="101" height="12" rx="6" fill="var(--yellow)"/>
    <rect x="9" y="107" width="100" height="12" rx="6" fill="var(--yellow)"/>
    <g fill="#c9c7b6">
      <circle cx="16" cy="45" r="6" fill="#b9b7a6"/><circle cx="37" cy="45" r="6" fill="#b9b7a6"/><circle cx="61" cy="45" r="6" fill="#b9b7a6"/>
      <circle cx="83" cy="45" r="6"/><circle cx="105" cy="45" r="6"/><circle cx="127" cy="45" r="6"/><circle cx="148" cy="45" r="6"/>
      <circle cx="16" cy="71" r="6"/><circle cx="37" cy="71" r="6"/><circle cx="61" cy="71" r="6"/><circle cx="83" cy="71" r="6"/><circle cx="105" cy="71" r="6"/><circle cx="127" cy="71" r="6"/><circle cx="148" cy="71" r="6"/>
      <circle cx="16" cy="97" r="6"/><circle cx="37" cy="97" r="6"/>
      <circle cx="127" cy="113" r="6"/><circle cx="148" cy="113" r="6"/>
      <circle cx="16" cy="139" r="6"/><circle cx="37" cy="139" r="6"/><circle cx="61" cy="139" r="6"/><circle cx="83" cy="139" r="6"/><circle cx="105" cy="139" r="6"/><circle cx="127" cy="139" r="6"/><circle cx="148" cy="139" r="6" fill="#dedccc"/>
    </g>
    <circle cx="61" cy="87" r="6" fill="#fff" stroke="var(--yellow)" stroke-width="1.5"/>
    <circle cx="105" cy="113" r="6" fill="#fff" stroke="var(--yellow)" stroke-width="1.5"/>
    <g fill="#fff">
      <text x="83" y="47">1</text><text x="105" y="47">2</text><text x="127" y="47">3</text><text x="148" y="47">4</text>
      <text x="16" y="73">5</text><text x="37" y="73">6</text><text x="61" y="73">7</text><text x="83" y="73">8</text><text x="105" y="73">9</text><text x="127" y="73">10</text><text x="148" y="73">11</text>
      <text x="16" y="99">12</text><text x="37" y="99">13</text><text x="83" y="89">15</text><text x="105" y="89">16</text><text x="127" y="89">17</text><text x="148" y="89">18</text>
      <text x="16" y="115">19</text><text x="37" y="115">20</text><text x="61" y="115">21</text><text x="83" y="115">22</text><text x="127" y="115">24</text><text x="148" y="115">25</text>
      <text x="16" y="141">26</text><text x="37" y="141">27</text><text x="61" y="141">28</text><text x="83" y="141">29</text><text x="105" y="141">30</text><text x="127" y="141">31</text><text x="148" y="141">1</text>
    </g>
    <text x="61" y="89" fill="var(--yellow-dark)">14</text>
    <text x="105" y="115" fill="var(--yellow-dark)">23</text>
  </svg>
</section>

<section class="abs panel visitors" style="left:427px">
  <h2>VISITORS</h2>
  <div class="abs total">Total Visitors</div>
  <div class="abs counter"><span>0</span><span>4</span><span>1</span><span>0</span><span>6</span><span>8</span><span>0</span><span>1</span></div>
  <div class="abs display join">JOIN US TODAY !</div>
  <div class="abs vrow" style="top:124px"><span class="abs lab">Parents</span><span class="abs cell" style="left:86px">9</span><span class="abs cell" style="left:103px">9</span><span class="abs cell" style="left:120px">+</span></div>
  <div class="abs vrow" style="top:146px"><span class="abs lab">Students</span><span class="abs cell" style="left:86px">9</span><span class="abs cell" style="left:103px">9</span><span class="abs cell" style="left:120px">+</span></div>
  <div class="abs vrow" style="top:168px"><span class="abs lab">Others</span><span class="abs cell" style="left:86px">9</span><span class="abs cell" style="left:103px">9</span><span class="abs cell" style="left:120px">+</span></div>
</section>

<div class="abs more-circle" style="left:166px"><svg width="10" height="10" viewBox="0 0 10 10"><path d="M4 1l4 4-4 4V6H1V4h3z" fill="#bbb8a5"/></svg></div>
<div class="abs more-circle" style="left:330px"><svg width="10" height="10" viewBox="0 0 10 10"><path d="M4 1l4 4-4 4V6H1V4h3z" fill="#bbb8a5"/></svg></div>
<div class="abs more-circle" style="left:494px"><svg width="10" height="10" viewBox="0 0 10 10"><path d="M4 1l4 4-4 4V6H1V4h3z" fill="#bbb8a5"/></svg></div>

<section class="abs promo" role="img" aria-label="Photo of a smiling schoolboy raising his hand in a bright classroom with a globe and pencils">
  <div class="abs display t1">SCHOOL</div>
  <div class="abs t2">Pri , High <b>edu</b></div>
  <div class="abs display t3">EDUCATIONAL</div>
  <div class="abs display t4"><small>for</small> ANY <small>kind</small> OF TEACHING !</div>
  <div class="abs more">MORE</div>
</section>
<div class="abs tab on" style="left:99px;width:99px">PRIMARY SCHOOL</div>
<div class="abs tab off" style="left:200px;width:104px">HIGH SCHOOL ( GIRLS )</div>
<div class="abs tab off" style="left:306px;width:104px">HIGH SCHOOL ( BOYS )</div>

<section class="abs finder">
  <div class="abs field" style="left:99px;width:127px">Keyword</div>
  <div class="abs field" style="left:237px;width:128px">Type<span style="position:absolute;right:8px;top:5px">⇕</span></div>
  <div class="abs field" style="left:375px;width:128px">Select<span style="position:absolute;right:8px;top:5px">⇕</span></div>
  <div class="abs send">SEND</div>
</section>

<footer class="abs footer">
  <h3 style="left:99px">CONTACT US !</h3>
  <div class="abs line" style="left:99px;width:124px"></div>
  <div class="abs input" style="top:65px;height:18px">NAME</div>
  <div class="abs input" style="top:86px;height:27px">EMAIL</div>
  <div class="abs fsend">SEND</div>

  <h3 style="left:273px">GALLERY PHOTOS !</h3>
  <div class="abs line" style="left:273px;width:112px"></div>
  <div class="abs gallery" role="img" aria-label="Grid of nine small school photos">
    <span style="background:#c98a6a"></span><span style="background:#e0a47c"></span><span style="background:#b9c7d6"></span>
    <span style="background:#9fc2df"></span><span style="background:#d9b16c"></span><span style="background:#d7c3a8"></span>
    <span style="background:#e3c79b"></span><span style="background:#a9b4c4"></span><span style="background:#e1a98f"></span>
  </div>

  <h3 style="left:428px">OTHER DETAILS !</h3>
  <div class="abs line" style="left:428px;width:100px;background:#dcdaca"></div>
  <div class="abs detail" style="top:56px"><svg width="8" height="8" viewBox="0 0 8 8"><path d="M1 0c1 0 1.5 1.5 1 2l-.5.5c.5 1.3 1.7 2.5 3 3L5 5c.5-.5 2 0 2 1v1C4 8-1 3 1 0z" fill="#888"/></svg><span class="v">124 (567) 8901</span></div>
  <div class="abs detail" style="top:84px"><svg width="9" height="7" viewBox="0 0 9 7"><rect x=".5" y=".5" width="8" height="6" fill="none" stroke="#888"/><path d="M.5 .5 4.5 4 8.5 .5" fill="none" stroke="#888"/></svg><span class="v">info@baytnakhla.edu</span></div>
  <div class="abs detail" style="top:112px"><svg width="8" height="7" viewBox="0 0 8 7"><path d="M0 3.5 4 0l4 3.5V7H0z" fill="#888"/></svg><span class="v">14 Palm Road Pa 30418</span></div>

  <div class="abs social-sq" style="top:49px;background:#5a5488"></div>
  <div class="abs social-sq" style="top:68px;background:#7b76a6"></div>
  <div class="abs social-sq" style="top:87px;background:#e0a646"></div>
  <div class="abs social-sq" style="top:106px;background:#c9893a"></div>
</footer>

<div class="abs copyright">© COPYRIGHT 2015. <b>BAYT NAKHLA SCHOOLS.</b> ALL RIGHTS RESERVED</div>

</body>
</html>
```